Memoir author looking for book cover design

Title:
"Rain, Rust and Return"

Subtitle:
"A Season Spent Chasing Our Father Across the Coastline"

My book is about the 18-month-long search and grieving process after my husband went missing from a hiking accident.
See "notesbeyondthequietharbor.example" for background

(An "ampersand" may look best, but I'm unable to enter it in this format)

Reason: Having difficulty finishing up, in part due to time difference. Don't want designers to have to work in the middle of the night!

```html
<!DOCTYPE html>
<html lang="en">
<head>
<meta charset="utf-8">
<title>Rain, Rust &amp; Return — Book Cover Wrap</title>
<link rel="stylesheet" href="https://fonts.googleapis.com/css2?family=Cinzel:wght@400;500&display=swap">
<style>
  :root {
    --ink-night: #050507;
    --earth-dark: #1f150b;
    --earth-warm: #6b4a1e;
    --spine-brown: #2a1e16;
    --spine-rope: #3d2b1f;
    --mint: #e3f5ef;
    --teal: #1e5f6a;
    --teal-deep: #16505a;
    --sky-blue: #4f6d80;
    --sunset-orange: #f08a3a;
    --sunset-gold: #f7c07a;
    --hill-dark: #1a1512;
  }
  * { margin: 0; padding: 0; box-sizing: border-box; }
  html, body { width: 1200px; height: 819px; overflow: hidden; background: #000; }
  .cover-wrap { position: relative; width: 1200px; height: 819px; font-family: "Cinzel", serif; color: var(--mint); }

  /* Back cover */
  .back-cover { position: absolute; left: 0; top: 0; width: 560px; height: 819px; overflow: hidden; }
  .back-artwork {
    position: absolute; inset: 0;
    background:
      radial-gradient(ellipse 60% 30% at 50% 85%, rgba(120,84,36,.75), transparent 70%),
      linear-gradient(to bottom, var(--ink-night) 0%, #0b0a0a 55%, var(--earth-dark) 80%, #120c06 100%);
  }
  .back-blurb {
    position: absolute; left: 84px; top: 160px; width: 390px;
    font-size: 12px; line-height: 39px; font-variant: small-caps; letter-spacing: .2px;
    color: var(--mint);
  }

  /* Spine */
  .spine {
    position: absolute; left: 560px; top: 0; width: 78px; height: 819px;
    background: linear-gradient(to right, var(--spine-brown), var(--spine-rope) 50%, var(--spine-brown));
    border-left: 1px solid #3a3a3a;
  }
  .spine-text {
    position: absolute; left: 50%; top: 24px; transform: translateX(-50%);
    writing-mode: vertical-rl; font-size: 31px; letter-spacing: 3px; white-space: nowrap;
    color: var(--mint); font-variant: small-caps;
  }
  .spine-text .spine-gap { display: inline-block; height: 36px; }

  /* Front cover */
  .front-cover { position: absolute; left: 638px; top: 0; width: 562px; height: 819px; overflow: hidden; }
  .front-artwork {
    position: absolute; inset: 0;
    background:
      linear-gradient(to bottom, transparent 60%, rgba(26,21,18,.9) 72%, var(--hill-dark) 100%),
      radial-gradient(ellipse 70% 25% at 50% 48%, var(--sunset-gold), transparent 70%),
      linear-gradient(to bottom, #3b4a57 0%, var(--sky-blue) 14%, #c9764a 26%, var(--sunset-orange) 40%, #d9703a 55%, #5a4a52 65%);
  }
  .author-name {
    position: absolute; left: 0; right: 0; top: 6px; text-align: center;
    font-size: 33px; letter-spacing: 4px; font-variant: small-caps; color: var(--mint);
    text-shadow: 0 1px 3px rgba(0,0,0,.35);
  }
  .book-title {
    position: absolute; left: 0; right: 0; top: 168px; text-align: center;
    font-size: 64px; font-weight: 400; line-height: 76px; color: var(--mint);
    text-shadow: 2px 3px 4px rgba(0,0,0,.6);
  }
  .title-rule { position: absolute; left: 28px; width: 508px; height: 2px; background: var(--teal); }
  .title-rule.upper { top: 240px; }
  .subtitle { position: absolute; left: 0; right: 0; top: 698px; text-align: center; }
  .subtitle-lead { display: block; font-size: 20px; font-variant: small-caps; color: var(--mint); letter-spacing: .5px; }
  .subtitle-key { display: block; font-size: 32px; letter-spacing: 10px; color: var(--teal-deep); margin-top: 2px; line-height: 38px; }
  .title-rule.lower { top: 770px; height: 1px; }
  .subtitle-tail { position: absolute; left: 0; right: 0; top: 778px; text-align: center; font-size: 19px; letter-spacing: 5px; color: var(--mint); }
</style>
</head>
<body>
<main class="cover-wrap">
  <section class="back-cover">
    <div class="back-artwork" role="img" aria-label="Starry night sky above dry golden grass, a pair of worn hiking boots with a blue butterfly resting on them and a small hummingbird"></div>
    <p class="back-blurb">Lorem ipsum dolor sit amet, consectetur adipisicing elit, sed do eiusmod tempor incididunt ut labore et dolore magna aliqua. Ut enim ad minim veniam, quis nostrud exercitation ullamco laboris nisi ut aliquip ex ea commodo consequat. Duis aute irure dolor in reprehenderit in voluptate velit esse cillum dolore eu fugiat nulla pariatur. Excepteur sint occaecat cupidatat non proident, sunt in culpa qui officia deserunt mollit anim id est laborum. Sed ut perspiciatis unde omnis iste natus error sit voluptatem accusantium doloremque.</p>
  </section>

  <section class="spine" role="img" aria-label="Spine with braided rope texture">
    <div class="spine-text">Dana Whitlow<span class="spine-gap"></span>RAIN, RUST &amp; RETURN</div>
  </section>

  <section class="front-cover">
    <div class="front-artwork" role="img" aria-label="Fiery orange sunset sky over forested mountain ridges with a bare tree and a flock of birds"></div>
    <p class="author-name">Dana Whitlow</p>
    <h1 class="book-title">RAIN, RUST<br>&amp; RETURN</h1>
    <div class="title-rule upper"></div>
    <p class="subtitle">
      <span class="subtitle-lead">A Season Spent Chasing</span>
      <span class="subtitle-key">OUR FATHER</span>
    </p>
    <div class="title-rule lower"></div>
    <p class="subtitle-tail">ACROSS THE COASTLINE</p>
  </section>
</main>
</body>
</html>
```